Local Finance and Insurance Advising Company from Switzerland needs an impressive banner design.

I am looking for an impressive Banner Design, I need this Banner for Facebook, LinkedIn, YouTube & Google.

I am Advising all kind of peoples who are living here in Switzerland. Young, middle age and old people. People who want to go study, people who are planning to create a family, old people who are, or going to retire. Expatriates who want to leave Switzerland to live in another country, expatriates who are coming to Switzerland. Peoples who ant to build their own business up. All kind of financial, insurance and pension planning's.

The Company Name is: Alpine Counsel
Our slogen / heading is: Clear Counsel, no Pitch

The Company logo can be used for the banner, but I would preffer to have the banner without logo, as the logo will be already in a another field on the social networks.

Since the first impression is the most important, this project is really important to me. I am ready to realize further projects with the one who can create the perfect banner who hits the point as described. I am a start-up company, everything is still on beginning and still much has to be done.

Target Market(s)

private clients

Requirements
Must have
• The banner should give the impression of happiness, safeness, health and freedom. Empowering people and creating freedom lifestyles.
Should not have
• I do not want that the banner looks like we are some kind of broker who is just selling some kind of insurances.

```html
<!DOCTYPE html>
<html lang="en">
<head>
<meta charset="utf-8">
<title>Alpine Counsel – Banner</title>
<link href="https://fonts.googleapis.com/css2?family=Jost:wght@400&family=Ubuntu:wght@500;700&display=swap" rel="stylesheet">
<style>
  :root {
    --brand-red: #e00a0a;
    --stripe-red: #ee1c0c;
    --title-grey: #7a7a7a;
    --ink: #1b1b1b;
    --paper: #ffffff;
    --mist: #eef2f1;
    --forest: #3f7a2c;
    --water: #4fa8a6;
  }
  * { margin: 0; padding: 0; box-sizing: border-box; }
  html, body { width: 1200px; height: 300px; overflow: hidden; background: var(--paper); }
  .banner { position: relative; width: 1200px; height: 300px; overflow: hidden; background: var(--paper); }
  .banner__art { position: absolute; inset: 0; width: 1200px; height: 300px; }
  .banner__copy {
    position: absolute; right: 61px; top: 38px;
    text-align: right;
  }
  .brand-name {
    font-family: "Jost", sans-serif; font-weight: 400;
    font-size: 66px; line-height: 1; letter-spacing: 1px;
    color: var(--title-grey); text-transform: uppercase;
  }
  .slogan {
    margin-top: 10px;
    font-family: "Ubuntu", sans-serif; font-weight: 700;
    font-size: 61px; line-height: 64px; letter-spacing: 1px;
    color: var(--brand-red); text-transform: uppercase;
  }
  .contact-bar {
    position: absolute; left: 645px; right: 61px; top: 261px;
    display: flex; justify-content: space-between; align-items: center;
    font-family: "Ubuntu", sans-serif; font-weight: 500; font-size: 12.5px;
    color: var(--ink);
  }
  .contact-item { display: flex; align-items: center; gap: 8px; }
  .contact-icon { width: 15px; height: 15px; flex: none; }
</style>
</head>
<body>
<div class="banner">
  <svg class="banner__art" viewBox="0 0 1200 300" xmlns="http://www.w3.org/2000/svg">
    <defs>
      <linearGradient id="sceneMist" x1="0" y1="0" x2="0" y2="1">
        <stop offset="0" stop-color="#ffffff"/>
        <stop offset="0.55" stop-color="#f3f6f4"/>
        <stop offset="0.9" stop-color="#e6eeec"/>
        <stop offset="1" stop-color="#9cc6c6"/>
      </linearGradient>
      <linearGradient id="sceneFalls" x1="0" y1="0" x2="0" y2="1">
        <stop offset="0" stop-color="#cfe3ee"/>
        <stop offset="0.25" stop-color="#3d7a2e"/>
        <stop offset="0.5" stop-color="#5c8a45"/>
        <stop offset="0.7" stop-color="#e9f0ef"/>
        <stop offset="0.92" stop-color="#d8e8e6"/>
        <stop offset="1" stop-color="#4fa8a6"/>
      </linearGradient>
    </defs>
    <rect class="scene-backdrop" x="0" y="0" width="1200" height="300" fill="url(#sceneMist)"
          role="img" aria-label="Faded photograph of a misty waterfall with a Swiss flag on the shore"/>
    <polygon class="scene-photo" points="0,18 494,62 574,300 0,300" fill="url(#sceneFalls)"
             role="img" aria-label="Photograph of a large waterfall with a wooded rock island, visitors and Swiss flags"/>
    <polygon class="accent-stripe" points="0,0 100,0 494,56 590,300 574,300 484,64 0,20" fill="var(--stripe-red)"/>
  </svg>

  <div class="banner__copy">
    <h1 class="brand-name">Alpine Counsel</h1>
    <p class="slogan">Clear Counsel<br>No Pitch</p>
  </div>

  <div class="contact-bar">
    <span class="contact-item">
      <svg class="contact-icon" viewBox="0 0 24 24"><path fill="var(--brand-red)" d="M6.6 2.5l3 3.6c.5.6.4 1.4-.1 1.9L8 9.5c1.2 2.6 3.8 5.3 6.5 6.5l1.5-1.5c.5-.5 1.3-.6 1.9-.1l3.6 3c.6.5.7 1.4.1 2l-1.9 2c-.9.9-2.3 1.2-3.5.7C9.4 19.8 4.2 14.6 1.9 7.8c-.4-1.2-.1-2.6.8-3.5l2-1.9c.6-.6 1.5-.5 1.9.1z"/></svg>
      +41-00-765-4321
    </span>
    <span class="contact-item">
      <svg class="contact-icon" viewBox="0 0 24 24"><rect x="1" y="4" width="22" height="16" fill="var(--brand-red)"/><path d="M1 4l11 9 11-9M1 20l8-8M23 20l-8-8" stroke="#fff" stroke-width="1.6" fill="none"/></svg>
      info@alpinecounsel.com
    </span>
    <span class="contact-item">
      <svg class="contact-icon" viewBox="0 0 24 24" fill="none" stroke="var(--brand-red)" stroke-width="1.8"><circle cx="12" cy="12" r="10.5"/><ellipse cx="12" cy="12" rx="4.5" ry="10.5"/><path d="M1.5 12h21M3.5 6.5h17M3.5 17.5h17M12 1.5v21"/></svg>
      www.alpinecounsel.com
    </span>
  </div>
</div>
</body>
</html>
```